HollowPine Ventures Inc. Business Card Design

My business is custom renovations and homes.I would need to have a new business logo created to go along with my company name. The business card should be of a modern style as this is the market I am focused on. I would need my contact information and website posted on the card. I would also like to list a few of the tasks I conduct on the card (such as: Renovations, Additions, Repairs, New Homes, Design, Consultations). On the reverse of the card I currently have just my logo and my motto, "Shaping A Bold Path". However, I am open to completely changing everything as I am starting a new year and would like to excel further. Any new ideas and suggestions are always welcomed. Thank you.

Target Market(s)

Upscale residential and commercial renovations and builds

Industry/Entity Type

Business

Contact Information for Business Card

I would like the design to be able to be laser cut or burnt onto a wooden business card. I will be creating one option of cards for really loyal customers (wooden) and a second option for the everyday customer (paper).

Font styles to use
Other font styles liked:
• Calibri / anything of mordern taste

Colors
f37122
5c5c5c
474747
ffffff

Requirements
Must have
• I would like the colours of my business to be a sharp orange and grey. I believe this will symbolize a modern style. I am open to other suggestions if this is not suitable for the designers tastes. My contact info as follows:
• Will Marsh
• President
• HollowPine Ventures Inc.
• 555-214-3987
• will@hollowpineventures.example
• I would like my website (currently under construction) hollowpineventures.example on the card aswell.
Nice to have
• Along with a modern logo representing HollowPine, I would like something on the card besides the logo and contact information. Perhaps a small background design. I feel it may be nice to have my services listed on the card (in smaller font on the bottom) Renovations, Additions, Repairs, Design, Consultations.
Should not have
• The business card should not have too many different colors. Should not have rounded corners.

```html
<!DOCTYPE html>
<html lang="en">
<head>
<meta charset="utf-8">
<title>HollowPine Ventures Inc. Business Card</title>
<link rel="stylesheet" href="https://fonts.googleapis.com/css2?family=Lato:wght@400;700&family=Roboto:wght@400&display=swap">
<style>
  :root {
    --orange: #f37122;
    --grey-text: #474747;
    --grey-mid: #5c5c5c;
    --card-dark: #333333;
    --white: #ffffff;
    --light-text: #e6e6e6;
    --backdrop: #d4d4d4;
  }
  * { margin: 0; padding: 0; box-sizing: border-box; }
  html, body { width: 1200px; height: 1000px; overflow: hidden; }
  body { background: var(--backdrop); position: relative; font-family: "Lato", sans-serif; }

  .card { position: absolute; width: 626px; box-shadow: 0 6px 18px rgba(0,0,0,0.35); }
  .card-front { left: 287px; top: 140px; height: 357px; background: var(--white); }
  .card-back { left: 287px; top: 531px; height: 358px; background: var(--card-dark); }

  .brand-square { position: absolute; background: var(--orange); }
  .card-front .brand-square { left: 103px; top: 122px; width: 130px; height: 110px; }
  .card-back .brand-square { left: 69px; top: 91px; width: 201px; height: 173px; }

  .divider { position: absolute; width: 2px; }
  .card-front .divider { left: 256px; top: 123px; height: 110px; background: var(--grey-mid); }
  .card-back .divider { left: 313px; top: 91px; height: 176px; background: var(--orange); }

  .company-name {
    position: absolute; left: 279px; top: 132px;
    font-family: "Lato", sans-serif; font-weight: 700; font-size: 33px; line-height: 44px;
    color: var(--grey-text);
  }

  .services {
    position: absolute; left: 0; right: 0; top: 302px; text-align: center;
    font-family: "Roboto", sans-serif; font-size: 15px; color: var(--grey-mid);
  }
  .services .sep { color: var(--orange); margin: 0 6px; }

  .contact { position: absolute; left: 332px; top: 88px; font-family: "Lato", sans-serif; color: var(--light-text); }
  .person-name { color: var(--orange); font-weight: 700; font-size: 19px; line-height: 24px; }
  .person-title { font-size: 14.5px; line-height: 18px; }
  .address { margin-top: 12px; font-size: 14.5px; line-height: 18px; }
  .contact-list { list-style: none; margin-top: 13px; font-size: 14.5px; line-height: 20px; }
  .contact-list li { display: flex; align-items: center; }
  .contact-list svg { width: 11px; height: 11px; margin-right: 9px; fill: var(--orange); flex: none; }
</style>
</head>
<body>

<section class="card card-front" aria-label="Business card front">
  <div class="brand-square"></div>
  <div class="divider"></div>
  <div class="company-name">HollowPine<br>Ventures Inc.</div>
  <p class="services">Renovations<span class="sep">|</span>Additions<span class="sep">|</span>Repairs<span class="sep">|</span>New Homes<span class="sep">|</span>Consultations</p>
</section>

<section class="card card-back" aria-label="Business card back">
  <div class="brand-square"></div>
  <div class="divider"></div>
  <div class="contact">
    <p class="person-name">Will Marsh</p>
    <p class="person-title">President</p>
    <p class="address">HollowPine Ventures Inc.<br>Street name, Suite 100<br>State, Zip Code, Country</p>
    <ul class="contact-list">
      <li><svg viewBox="0 0 24 24" aria-hidden="true"><path d="M6.6 10.8a15.1 15.1 0 0 0 6.6 6.6l2.2-2.2c.3-.3.7-.4 1-.2 1.1.4 2.3.6 3.6.6.6 0 1 .4 1 1V20c0 .6-.4 1-1 1A17 17 0 0 1 3 4c0-.6.4-1 1-1h3.5c.6 0 1 .4 1 1 0 1.3.2 2.5.6 3.6.1.3 0 .7-.2 1z"/></svg>555-214-3987</li>
      <li><svg viewBox="0 0 24 24" aria-hidden="true"><path d="M2 5h20v14H2z M2 5l10 7 10-7" /></svg>will@hollowpineventures.example</li>
      <li><svg viewBox="0 0 24 24" aria-hidden="true"><path d="M12 2a10 10 0 1 0 0 20 10 10 0 0 0 0-20zm6.9 6h-3a15.6 15.6 0 0 0-1.4-3.6A8 8 0 0 1 18.9 8zM12 4c.8 1.2 1.5 2.5 1.9 4h-3.8c.4-1.5 1.1-2.8 1.9-4zM4.3 14a8.2 8.2 0 0 1 0-4h3.4a16 16 0 0 0 0 4zm.8 2h3a15.6 15.6 0 0 0 1.4 3.6A8 8 0 0 1 5.1 16zm3-8h-3a8 8 0 0 1 4.4-3.6C8.9 5.5 8.4 6.7 8.1 8zM12 20c-.8-1.2-1.5-2.5-1.9-4h3.8c-.4 1.5-1.1 2.8-1.9 4zm2.3-6H9.7a14.7 14.7 0 0 1 0-4h4.6a14.7 14.7 0 0 1 0 4zm.2 5.6c.6-1.1 1.1-2.3 1.4-3.6h3a8 8 0 0 1-4.4 3.6zm1.8-5.6a16 16 0 0 0 0-4h3.4a8.2 8.2 0 0 1 0 4z"/></svg>hollowpineventures.example</li>
    </ul>
  </div>
</section>

</body>
</html>
```